Kornfeldtakt.de

The ostwind-tauschhalle.de (oth) is an internet portal for the incurance industry in Germany: www.ostwind-tauschhalle.de.

We are now planning to start a new brand Kornfeldtakt.de, which will be integral part of oth, but will have own logo, navigation etc. The main topic of Kornfeldtakt.de will be the new digital way of communication between insurance companies and insurance brokers (selling companies' products).

The main content of Kornfeldtakt.de will consist of articles / blog entries and at this moment we would like to concentrate on that part of our new brand.

At the top of the page we will always have a cover story, which will be the latest published article.

Under the cover story the user will find other articles. The articles should have variable widths (1/3, 2/3, 3/3). We will also need some additional elements like newsletter subscription, articles with most clicks etc.

Please use as reference this page:
https://www.brenntal.de/

We really like how it is designed.

Here you will find the current state of our project:

https://relaunch.ostwind-tauschhalle.de/kornfeldtakt

We will also need a logo for Kornfeldtakt.de, which should include the subtitle: Immer unabhängig, niemals neutral AND powerd by ostwind-tauschhalle.de

Due to the problems with the "Pool" functionality at Formbazaar we will need more time to verify your projects in our teem - but we are on it.

```html
<!DOCTYPE html>
<html lang="en">
<head>
<meta charset="utf-8">
<title>Kornfeldtakt.de – Articles</title>
<link href="https://fonts.googleapis.com/css2?family=Poppins:ital,wght@0,400;0,500;0,600;0,700;1,400&display=swap" rel="stylesheet">
<style>
:root{
  --red:#e3262b;
  --ink:#1c1c1c;
  --text:#444;
  --muted:#8a8a8a;
  --line:#e6e6e6;
  --white:#fff;
  --footer:#0b0b0b;
  --hero-a:#3b3a3c;
  --hero-b:#8d8a86;
}
*{box-sizing:border-box;margin:0;padding:0}
html,body{width:1200px;height:4364px;overflow:hidden}
body{font-family:'Poppins',sans-serif;color:var(--ink);background:var(--white);position:relative}
.abs{position:absolute}
a{color:inherit;text-decoration:none}

/* header */
.topstrip{top:0;left:660px;width:540px;height:26px;background:var(--red);display:flex;justify-content:flex-end;align-items:center;gap:26px;padding-right:40px;color:#fff;font-size:10px;font-weight:600;letter-spacing:.5px}
.topstrip span{display:flex;align-items:center;gap:6px}
.brand{top:30px;left:80px}
.brand-name{display:block;color:var(--red);font-weight:700;font-size:24px;line-height:1.1;letter-spacing:.5px}
.brand-tagline{display:block;font-size:9px;line-height:1.35;color:var(--muted);font-weight:500;margin-top:3px}
.mainnav{top:60px;right:80px;display:flex;align-items:center;gap:34px;font-size:12px;font-weight:600;color:#333}
.searchbtn{width:30px;height:30px;border-radius:50%;background:#555;display:flex;align-items:center;justify-content:center}

/* hero */
.hero{top:112px;left:0;width:1200px;height:488px;background:linear-gradient(100deg,var(--hero-a) 0%,#5f5d5c 45%,var(--hero-b) 100%)}
.hero-copy{position:absolute;left:80px;top:120px;color:#fff;width:520px}
.hero-kicker{font-size:20px;letter-spacing:4px;font-weight:500}
.hero-title{font-size:44px;line-height:1.12;font-weight:700;margin-top:4px}
.hero-sub{font-size:15px;font-weight:600;margin-top:14px;line-height:1.5}
.btn-red{display:inline-block;background:var(--red);color:#fff;font-size:11px;font-weight:700;padding:11px 26px;margin-top:28px;letter-spacing:.3px}
.hero-arrow{position:absolute;top:248px;width:28px;height:48px;background:#444;display:flex;align-items:center;justify-content:center}

/* section heads */
.sec-head{left:80px;width:1040px;display:flex;justify-content:space-between;align-items:center}
.sec-head h2{font-size:34px;font-weight:600;color:var(--ink)}
.btn-outline{border:1.5px solid var(--red);color:var(--red);font-size:11px;font-weight:700;padding:11px 28px;letter-spacing:.5px}

/* cards */
.tag{display:inline-block;background:var(--red);color:#fff;font-size:8px;font-weight:700;padding:4px 9px;letter-spacing:.4px}
.card-grid{left:80px;width:1040px;display:grid;grid-template-columns:repeat(3,1fr);gap:32px 12px}
.card{background:#fff;box-shadow:0 4px 18px rgba(0,0,0,.1);height:508px}
.ph{display:block;width:100%}
.card .ph{height:210px}
.card-body{padding:22px 22px 0}
.card-title{font-size:17px;font-weight:600;line-height:1.35;margin-top:12px}
.card-excerpt{font-size:13px;font-style:italic;color:var(--text);line-height:1.55;margin-top:12px}
.more{color:var(--red);font-size:11px;font-weight:700;margin-top:14px;display:flex;align-items:center;gap:6px;letter-spacing:.3px}
.meta{display:flex;justify-content:space-between;align-items:center;font-size:11px;color:#555;border-top:1px solid var(--line);margin-top:20px;padding-top:16px}
.meta span{display:flex;align-items:center;gap:6px}

/* top article */
.top-block{top:2072px;left:80px;width:1040px;height:528px}
.top-main{position:absolute;left:0;top:0;width:440px;height:528px}
.overlay-text{position:absolute;left:22px;bottom:30px;right:22px;color:#fff}
.overlay-text .title{font-size:20px;font-weight:600;line-height:1.35;margin-top:10px}
.top-mid{position:absolute;left:448px;top:0;width:284px;display:flex;flex-direction:column;gap:8px}
.top-mid .ph{height:170px}
.top-list{position:absolute;left:748px;top:16px;width:292px;display:flex;flex-direction:column;gap:36px}
.mini-title{font-size:14px;font-weight:600;line-height:1.4;margin-top:10px}
.mini-meta{display:flex;justify-content:space-between;font-size:10px;color:#555;margin-top:10px}
.mini-meta span{display:flex;align-items:center;gap:5px}

/* events */
.events{top:2752px;left:80px;width:1040px;display:grid;grid-template-columns:1fr 1fr;gap:12px}
.event .ph{height:210px}
.event-body{padding-top:20px}
.event-title{font-size:16px;font-weight:600;line-height:1.4;margin-top:12px}
.event-text{font-size:13px;color:var(--text);line-height:1.6;margin-top:10px}

/* general */
.gen-left{top:3432px;left:80px;width:350px}
.gen-left .ph{height:226px}
.gen-left .card-title{font-size:18px}
.gen-grid{top:3432px;left:444px;width:660px;display:grid;grid-template-columns:repeat(3,1fr);gap:10px}
.tile{position:relative;height:196px}
.tile .ph{height:196px}
.tile .overlay-text{left:14px;right:14px;bottom:16px}
.tile .overlay-text .title{font-size:12px;margin-top:6px;line-height:1.35}

/* newsletter + footer */
.footer{top:4000px;left:0;width:1200px;height:364px;background:var(--footer);color:#fff}
.newsletter{top:3940px;left:184px;width:916px;height:120px;background:var(--red);display:flex;align-items:center;padding:0 44px;gap:40px;color:#fff}
.nl-label small{display:block;font-size:12px}
.nl-label strong{font-size:24px;font-weight:600}
.nl-input{width:316px;height:42px;background:#fff;color:#777;font-size:12px;display:flex;align-items:center;padding:0 16px}
.nl-btn{height:42px;background:#111;color:#fff;font-size:11px;font-weight:700;display:flex;align-items:center;padding:0 30px;margin-left:-28px}
.foot-brand{position:absolute;left:80px;top:100px;width:420px}
.foot-brand .brand-name{font-size:22px}
.foot-brand .brand-tagline{color:#999}
.foot-about{font-size:12px;color:#bbb;line-height:1.6;margin-top:12px}
.copyright{position:absolute;left:80px;top:336px;font-size:11px;color:#bbb}
.foot-col{position:absolute;top:100px}
.foot-col h4{font-size:17px;font-weight:600;margin-bottom:14px}
.quick{left:572px}
.quick ul{list-style:none;display:grid;grid-template-columns:110px 110px;gap:8px 0;font-size:11px;color:#ccc}
.quick li{display:flex;align-items:center;gap:8px}
.quick li::before{content:"";width:4px;height:4px;background:var(--red);border-radius:50%}
.divider{position:absolute;top:100px;width:1px;height:200px;background:#333}
.social{left:900px}
.social ul{list-style:none;display:flex;flex-direction:column;gap:14px;font-size:12px;color:#ccc}
.social li{display:flex;align-items:center;gap:12px}
.social .dot{width:26px;height:26px;border-radius:50%;background:var(--red)}
</style>
</head>
<body>

<!-- header -->
<div class="abs topstrip">
  <span><svg width="10" height="10" viewBox="0 0 10 10"><rect x="1" y="1" width="8" height="8" fill="none" stroke="#fff" stroke-width="1.4"/></svg>MEDIA DATA</span>
  <span><svg width="11" height="9" viewBox="0 0 11 9"><rect x=".7" y=".7" width="9.6" height="7.6" fill="none" stroke="#fff" stroke-width="1.3"/><path d="M1 1l4.5 4 4.5-4" fill="none" stroke="#fff" stroke-width="1.3"/></svg>NEWSLETTER</span>
  <span><svg width="10" height="10" viewBox="0 0 10 10"><circle cx="5" cy="3" r="2.3" fill="#fff"/><path d="M0.5 10a4.5 4 0 0 1 9 0z" fill="#fff"/></svg>LOGIN</span>
</div>
<div class="abs brand">
  <span class="brand-name">KORNFELDTAKT</span>
  <span class="brand-tagline">Immer unabhängig, niemals neutral<br>powered by ostwind-tauschhalle.de</span>
</div>
<nav class="abs mainnav">
  <a>PROCESS MESSAGES</a><a>MVP SYSTEMS</a><a>EVENTS</a><a>STUDIES</a>
  <span class="searchbtn"><svg width="13" height="13" viewBox="0 0 13 13"><circle cx="5.5" cy="5.5" r="4" fill="none" stroke="#fff" stroke-width="1.6"/><path d="M8.5 8.5l3.5 3.5" stroke="#fff" stroke-width="1.6"/></svg></span>
</nav>

<!-- hero -->
<section class="abs hero" role="img" aria-label="Photo of a business man in a suit reading documents at a desk">
  <div class="hero-copy">
    <div class="hero-kicker">CHANGE OF</div>
    <h1 class="hero-title">Leadership In The Executive Floors</h1>
    <p class="hero-sub">The personnel carousel is turning again in the new year: Halvora, Feldmark Germany, MC Arno Lindqvist</p>
    <a class="btn-red">CONTINUE READING</a>
  </div>
  <span class="hero-arrow" style="left:0"><svg width="10" height="14" viewBox="0 0 10 14"><path d="M8 1L2 7l6 6" fill="none" stroke="#fff" stroke-width="2"/></svg></span>
  <span class="hero-arrow" style="right:0"><svg width="10" height="14" viewBox="0 0 10 14"><path d="M2 1l6 6-6 6" fill="none" stroke="#fff" stroke-width="2"/></svg></span>
</section>

<!-- feature article -->
<div class="abs sec-head" style="top:746px"><h2>Feature Article</h2><a class="btn-outline">LOAD MORE</a></div>
<div class="abs card-grid" style="top:832px">
  <article class="card">
    <div class="ph" role="img" aria-label="Photo of a team meeting around a table from above" style="background:linear-gradient(135deg,#6b5a48,#c7b79f)"></div>
    <div class="card-body"><span class="tag">CATEGORIES</span>
      <h3 class="card-title">Change of leadership in the executive floors</h3>
      <p class="card-excerpt">Nordlicht expands its board of directors and fills the newly created "Custom-er and Innovation Management"...</p>
      <div class="more">CONTINUE READING <svg width="12" height="8" viewBox="0 0 12 8"><path d="M0 4h10M7 1l3 3-3 3" fill="none" stroke="#e3262b" stroke-width="1.5"/></svg></div>
      <div class="meta"><span><svg width="11" height="11" viewBox="0 0 11 11"><rect x="1" y="2" width="9" height="8" fill="none" stroke="#333" stroke-width="1.2"/><path d="M1 4.5h9" stroke="#333"/></svg>27 May 2021</span><span><svg width="12" height="10" viewBox="0 0 12 10"><path d="M1 1h10v6H5l-3 2V7H1z" fill="#333"/></svg>205</span></div>
    </div>
  </article>
  <article class="card">
    <div class="ph" role="img" aria-label="Photo of modern office towers seen from below" style="background:linear-gradient(160deg,#dfe3e8,#8e99a6)"></div>
    <div class="card-body"><span class="tag">CATEGORIES</span>
      <h3 class="card-title">Change of leadership in the executive floors</h3>
      <p class="card-excerpt">Nordlicht expands its board of directors and fills the newly created "Custom-er and Innovation Management"...</p>
      <div class="more">CONTINUE READING <svg width="12" height="8" viewBox="0 0 12 8"><path d="M0 4h10M7 1l3 3-3 3" fill="none" stroke="#e3262b" stroke-width="1.5"/></svg></div>
      <div class="meta"><span><svg width="11" height="11" viewBox="0 0 11 11"><rect x="1" y="2" width="9" height="8" fill="none" stroke="#333" stroke-width="1.2"/><path d="M1 4.5h9" stroke="#333"/></svg>27 May 2021</span><span><svg width="12" height="10" viewBox="0 0 12 10"><path d="M1 1h10v6H5l-3 2V7H1z" fill="#333"/></svg>205</span></div>
    </div>
  </article>
  <article class="card">
    <div class="ph" role="img" aria-label="Photo of colleagues discussing at a desk" style="background:linear-gradient(135deg,#8c7a66,#d9cdbb)"></div>
    <div class="card-body"><span class="tag">CATEGORIES</span>
      <h3 class="card-title">Change of leadership in the executive floors</h3>
      <p class="card-excerpt">Nordlicht expands its board of directors and fills the newly created "Custom-er and Innovation Management"...</p>
      <div class="more">CONTINUE READING <svg width="12" height="8" viewBox="0 0 12 8"><path d="M0 4h10M7 1l3 3-3 3" fill="none" stroke="#e3262b" stroke-width="1.5"/></svg></div>
      <div class="meta"><span><svg width="11" height="11" viewBox="0 0 11 11"><rect x="1" y="2" width="9" height="8" fill="none" stroke="#333" stroke-width="1.2"/><path d="M1 4.5h9" stroke="#333"/></svg>27 May 2021</span><span><svg width="12" height="10" viewBox="0 0 12 10"><path d="M1 1h10v6H5l-3 2V7H1z" fill="#333"/></svg>205</span></div>
    </div>
  </article>
  <article class="card">
    <div class="ph" role="img" aria-label="Photo of printed charts and a laptop on a desk" style="background:linear-gradient(135deg,#9aa8b6,#e4e0d6)"></div>
    <div class="card-body"><span class="tag">CATEGORIES</span>
      <h3 class="card-title">Change of leadership in the executive floors</h3>
      <p class="card-excerpt">Nordlicht expands its board of directors and fills the newly created "Custom-er and Innovation Management"...</p>
      <div class="more">CONTINUE READING <svg width="12" height="8" viewBox="0 0 12 8"><path d="M0 4h10M7 1l3 3-3 3" fill="none" stroke="#e3262b" stroke-width="1.5"/></svg></div>
      <div class="meta"><span><svg width="11" height="11" viewBox="0 0 11 11"><rect x="1" y="2" width="9" height="8" fill="none" stroke="#333" stroke-width="1.2"/><path d="M1 4.5h9" stroke="#333"/></svg>27 May 2021</span><span><svg width="12" height="10" viewBox="0 0 12 10"><path d="M1 1h10v6H5l-3 2V7H1z" fill="#333"/></svg>205</span></div>
    </div>
  </article>
  <article class="card">
    <div class="ph" role="img" aria-label="Photo of a brick office building under a blue sky" style="background:linear-gradient(180deg,#7fa6d0,#a56e4e)"></div>
    <div class="card-body"><span class="tag">CATEGORIES</span>
      <h3 class="card-title">Change of leadership in the executive floors</h3>
      <p class="card-excerpt">Nordlicht expands its board of directors and fills the newly created "Custom-er and Innovation Management"...</p>
      <div class="more">CONTINUE READING <svg width="12" height="8" viewBox="0 0 12 8"><path d="M0 4h10M7 1l3 3-3 3" fill="none" stroke="#e3262b" stroke-width="1.5"/></svg></div>
      <div class="meta"><span><svg width="11" height="11" viewBox="0 0 11 11"><rect x="1" y="2" width="9" height="8" fill="none" stroke="#333" stroke-width="1.2"/><path d="M1 4.5h9" stroke="#333"/></svg>27 May 2021</span><span><svg width="12" height="10" viewBox="0 0 12 10"><path d="M1 1h10v6H5l-3 2V7H1z" fill="#333"/></svg>205</span></div>
    </div>
  </article>
  <article class="card">
    <div class="ph" role="img" aria-label="Photo of a business meeting in a bright office" style="background:linear-gradient(135deg,#c9c2b6,#6d655c)"></div>
    <div class="card-body"><span class="tag">CATEGORIES</span>
      <h3 class="card-title">Change of leadership in the executive floors</h3>
      <p class="card-excerpt">Nordlicht expands its board of directors and fills the newly created "Custom-er and Innovation Management"...</p>
      <div class="more">CONTINUE READING <svg width="12" height="8" viewBox="0 0 12 8"><path d="M0 4h10M7 1l3 3-3 3" fill="none" stroke="#e3262b" stroke-width="1.5"/></svg></div>
      <div class="meta"><span><svg width="11" height="11" viewBox="0 0 11 11"><rect x="1" y="2" width="9" height="8" fill="none" stroke="#333" stroke-width="1.2"/><path d="M1 4.5h9" stroke="#333"/></svg>27 May 2021</span><span><svg width="12" height="10" viewBox="0 0 12 10"><path d="M1 1h10v6H5l-3 2V7H1z" fill="#333"/></svg>205</span></div>
    </div>
  </article>
</div>

<!-- top article -->
<div class="abs sec-head" style="top:1966px"><h2>Top Article</h2><a class="btn-outline">LOAD MORE</a></div>
<div class="abs top-block">
  <div class="top-main ph" role="img" aria-label="Photo of a smiling man in a suit in an office" style="background:linear-gradient(180deg,#9a9792 0%,#5a5856 60%,#1e1e1e 100%)">
    <div class="overlay-text"><span class="tag">CATEGORIES</span><div class="title">Change in the management of Ostwind-tauschhalle.de</div></div>
  </div>
  <div class="top-mid">
    <div class="ph" role="img" aria-label="Photo of hands working on a laptop" style="background:linear-gradient(135deg,#4c5a52,#b7b3a8)"></div>
    <div class="ph" role="img" aria-label="Photo of a team meeting with notes on a table" style="background:linear-gradient(135deg,#cfc7bb,#7e6a56)"></div>
    <div class="ph" role="img" aria-label="Photo of hands holding a smartphone" style="background:linear-gradient(135deg,#b89b82,#57606a)"></div>
  </div>
  <div class="top-list">
    <div><span class="tag">CATEGORIES</span><div class="mini-title">Sed ut perspiciatis unde omnis iste natus error</div><div class="mini-meta"><span>27 May 2021</span><span><svg width="12" height="10" viewBox="0 0 12 10"><path d="M1 1h10v6H5l-3 2V7H1z" fill="#333"/></svg>205</span></div></div>
    <div><span class="tag">CATEGORIES</span><div class="mini-title">Sed ut perspiciatis unde omnis iste natus error</div><div class="mini-meta"><span>27 May 2021</span><span><svg width="12" height="10" viewBox="0 0 12 10"><path d="M1 1h10v6H5l-3 2V7H1z" fill="#333"/></svg>205</span></div></div>
    <div><span class="tag">CATEGORIES</span><div class="mini-title">Sed ut perspiciatis unde omnis iste natus error</div><div class="mini-meta"><span>27 May 2021</span><span><svg width="12" height="10" viewBox="0 0 12 10"><path d="M1 1h10v6H5l-3 2V7H1z" fill="#333"/></svg>205</span></div></div>
  </div>
</div>

<!-- recent events -->
<div class="abs sec-head" style="top:2666px"><h2>Recent Events</h2><a class="btn-outline">LOAD MORE</a></div>
<div class="abs events">
  <article class="event">
    <div class="ph" role="img" aria-label="Photo of a keyboard and desk in a dark office" style="background:linear-gradient(135deg,#2f2a26,#a08a74)"></div>
    <div class="event-body"><span class="tag">EVENTS</span>
      <h3 class="event-title">Clarification: Ulmbach Versicherung was not the victim of a cyber attack.</h3>
      <p class="event-text">We would like to point out that the company is not Ulmbach Versicherung, but Ulmbach AG, which is a leading supplier of digital industrial content. When selecting the item we read out...</p>
      <div class="meta"><span>27 May 2021</span><span><svg width="12" height="10" viewBox="0 0 12 10"><path d="M1 1h10v6H5l-3 2V7H1z" fill="#333"/></svg>205</span></div>
    </div>
  </article>
  <article class="event">
    <div class="ph" role="img" aria-label="Photo of a group of delegates talking at a table" style="background:linear-gradient(135deg,#a7958a,#4f4440)"></div>
    <div class="event-body"><span class="tag">EVENTS</span>
      <h3 class="event-title">VDM Assembly of Delegates: Executive Committee re-elected. Structural reform and lead motion...</h3>
      <p class="event-text">At the delegates' meeting to mark the 125th anniversary of the Federal Union of Independent Policy Traders (VDM) on November 11 in Hamburg, VDM President Jonas R...</p>
      <div class="meta"><span>27 May 2021</span><span><svg width="12" height="10" viewBox="0 0 12 10"><path d="M1 1h10v6H5l-3 2V7H1z" fill="#333"/></svg>205</span></div>
    </div>
  </article>
</div>

<!-- general article -->
<div class="abs sec-head" style="top:3342px"><h2>General Article</h2><a class="btn-outline">LOAD MORE</a></div>
<article class="abs gen-left">
  <div class="ph" role="img" aria-label="Photo of a woman working on a laptop at a desk" style="background:linear-gradient(135deg,#d8cab8,#8a7260)"></div>
  <div style="padding-top:18px"><span class="tag">CATEGORIES</span>
    <h3 class="card-title">Change of leadership in the executive floors</h3>
  </div>
</article>
<div class="abs gen-grid">
  <div class="tile"><div class="ph" role="img" aria-label="Photo of a business man in an office" style="background:linear-gradient(180deg,#8b8884,#2a2a2a)"></div><div class="overlay-text"><span class="tag">CATEGORIES</span><div class="title">Sed ut perspiciatis unde omnis iste natus error totam rem aperiam</div></div></div>
  <div class="tile"><div class="ph" role="img" aria-label="Photo of two women reviewing papers" style="background:linear-gradient(180deg,#9e8f82,#2c2723)"></div><div class="overlay-text"><span class="tag">CATEGORIES</span><div class="title">Sed ut perspiciatis unde omnis iste natus error totam rem aperiam</div></div></div>
  <div class="tile"><div class="ph" role="img" aria-label="Photo of a meeting room with large windows" style="background:linear-gradient(180deg,#a49077,#2a231d)"></div><div class="overlay-text"><span class="tag">CATEGORIES</span><div class="title">Sed ut perspiciatis unde omnis iste natus error totam rem aperiam</div></div></div>
  <div class="tile"><div class="ph" role="img" aria-label="Photo of colleagues at a desk with a laptop" style="background:linear-gradient(180deg,#8d8278,#262220)"></div><div class="overlay-text"><span class="tag">CATEGORIES</span><div class="title">Sed ut perspiciatis unde omnis iste natus error totam rem aperiam</div></div></div>
  <div class="tile"><div class="ph" role="img" aria-label="Photo of a team around a conference table" style="background:linear-gradient(180deg,#b2a496,#2f2925)"></div><div class="overlay-text"><span class="tag">CATEGORIES</span><div class="title">Sed ut perspiciatis unde omnis iste natus error totam rem aperiam</div></div></div>
  <div class="tile"><div class="ph" role="img" aria-label="Photo of a modern office interior" style="background:linear-gradient(180deg,#7c7672,#1f1d1c)"></div><div class="overlay-text"><span class="tag">CATEGORIES</span><div class="title">Sed ut perspiciatis unde omnis iste natus error totam rem aperiam</div></div></div>
</div>

<!-- footer -->
<footer class="abs footer">
  <div class="foot-brand">
    <span class="brand-name">KORNFELDTAKT</span>
    <span class="brand-tagline">Immer unabhängig, niemals neutral · powered by ostwind-tauschhalle.de</span>
    <p class="foot-about">Lorem ipsum dolor sit amet, consectetur adipiscing elit sed do eiusmod tempor incidi ut labore et dolore magna aliqua ut enim.</p>
  </div>
  <div class="copyright">© Copyright 2021 Kornfeldtakt</div>
  <div class="divider" style="left:540px"></div>
  <div class="foot-col quick"><h4>Quick Links</h4>
    <ul><li>Conditions</li><li>Sitemap</li><li>Privacy</li><li>Team</li><li>Help</li><li>Media</li><li>Imprint</li><li>Jobs</li></ul>
  </div>
  <div class="divider" style="left:868px"></div>
  <div class="foot-col social"><h4>Stay With Us</h4>
    <ul><li><span class="dot"></span>Friendwall</li><li><span class="dot"></span>Chirper</li><li><span class="dot"></span>Snapgram</li></ul>
  </div>
</footer>
<div class="abs newsletter">
  <div class="nl-label"><small>Newsletter</small><strong>Subscribe Us</strong></div>
  <div class="nl-input">Email Address</div>
  <div class="nl-btn">SUBSCRIBE&nbsp;<svg width="12" height="8" viewBox="0 0 12 8"><path d="M0 4h10M7 1l3 3-3 3" fill="none" stroke="#fff" stroke-width="1.5"/></svg></div>
</div>

</body>
</html>
```